BRIMWAVE.live*

I am needing a web site built for the main purpose of uploading podcasts
(MP3 files) to be viewed by large audiences of 1000+ site visitors on a regular basis. I have created a rough draft of how I want the site to look.

i have created a rough draft of the home page - the LOGO for this site is a spectacular lightening bolt which appears on my home page sample... the file for this image I purchased is too large to download to your site. I will supply on reuquest.

There will be 5 pages; HOME ABOUT RESOURCES DEVOTIONALS MORTY.
I have all the content prepared for each of the above pages.

Target Market(s)

All people groups seeking positive and encouraging words, life lessons and testimonies of faith.

Coding

Coded - Design and coding required

Number of Pages Required

1 page

Colors
3176b5

Requirements
Must have
• The design and layout provided - my sample

Black backgrounds as shown on my sample

```html
<!DOCTYPE html>
<html lang="en">
<head>
<meta charset="utf-8">
<title>BRIMWAVE.live</title>
<link href="https://fonts.googleapis.com/css2?family=Playfair+Display:wght@700;800&family=League+Spartan:wght@300;400;500;600&family=Roboto:wght@400;500&display=swap" rel="stylesheet">
<style>
:root{
  --black:#000;
  --ink:#231f20;
  --blue:#3176b5;
  --red:#e42d2f;
  --paper:#f2f5f8;
  --white:#fff;
  --grey:#a9a7a8;
  --body:#6b6b6b;
  --serif:'Playfair Display', Georgia, serif;
  --sans:'League Spartan', Arial, sans-serif;
  --nav:'Roboto', Arial, sans-serif;
}
*{margin:0;padding:0;box-sizing:border-box}
html,body{width:686px;height:1200px;overflow:hidden;background:var(--black)}
.page{position:relative;width:686px;height:1200px;overflow:hidden;font-family:var(--sans)}
.abs{position:absolute}

/* header */
.site-header{left:0;top:0;width:686px;height:45px;background:var(--black);border-bottom:1px solid #2b2b2b}
.nav-link{top:21px;font-family:var(--nav);font-size:9.5px;color:var(--red);letter-spacing:.2px}
.nav-link.active{color:var(--blue)}
.nav-underline{left:50px;top:44px;width:37px;height:1.5px;background:var(--blue)}
.wordmark{font-family:var(--serif);font-weight:800;color:var(--white);white-space:nowrap}
.header-mark{left:0;width:686px;text-align:center;top:10px;font-size:19px}

/* hero */
.hero{left:0;top:45px;width:686px;height:275px;background:var(--black)}
.hero-text{left:510px;top:152px;width:170px;text-align:center;font-family:var(--serif);font-weight:800;color:var(--white);font-size:17.5px;line-height:22px;letter-spacing:.5px}

/* about */
.about{left:0;top:320px;width:686px;height:210px;background:var(--ink)}
.section-title{font-family:var(--serif);font-weight:800;font-size:21px;color:var(--blue);letter-spacing:.8px}
.about-title{left:0;top:30px;width:686px;text-align:center}
.about-copy{left:90px;top:65px;width:506px;text-align:center;font-size:7.6px;line-height:11px;color:var(--grey);font-weight:300}
.about-copy p+p{margin-top:11px}
.btn{border-radius:12px;color:var(--white);font-size:6.4px;font-weight:600;letter-spacing:.6px;display:flex;align-items:center;justify-content:center}
.btn-discover{left:302px;top:151px;width:82px;height:23px;background:var(--red)}

/* light area */
.light{left:0;top:530px;width:686px;height:464px;background:var(--paper)}
.episodes{left:18px;top:549px;width:650px;height:137px;display:flex}
.episode{position:relative;flex:1;background:var(--black);border-right:1px solid #333;text-align:center;color:var(--white)}
.episode:last-child{border-right:none}
.episode.featured{background:var(--blue)}
.episode svg{position:absolute;left:48px;top:27px}
.episode-date{position:absolute;left:0;width:100%;top:73px;font-size:7.4px;color:var(--blue);font-weight:500}
.episode.featured .episode-date{color:var(--white)}
.episode-title{position:absolute;left:0;width:100%;top:84px;font-size:9.6px;line-height:14px;font-weight:500}
.episode-bar{position:absolute;left:31px;bottom:0;width:68px;height:2px;background:var(--blue)}
.episode.featured .episode-bar{display:none}

.pastor-title{left:50px;top:738px;font-size:21px;white-space:nowrap}
.pastor-title .role{color:var(--red)}
.pastor-title .dash{color:var(--blue);font-weight:700}
.pastor-copy{left:50px;top:772px;width:285px;font-size:7.8px;line-height:11px;color:var(--body);font-weight:300}
.pastor-copy p+p{margin-top:11px}
.btn-explore{left:50px;top:880px;width:82px;height:23px;background:var(--blue)}
.pastor-frame{left:389px;top:741px;width:228px;height:182px;border:1.5px solid var(--red)}
.pastor-photo{left:407px;top:722px;width:229px;height:183px;background:linear-gradient(135deg,#5a5a5a,#9a9a9a 45%,#3d3d3d)}

/* subscribe */
.subscribe{left:18px;top:961px;width:650px;height:68px;background:var(--blue)}
.subscribe-text{left:74px;top:23px;font-size:13.5px;color:var(--white);font-weight:400;white-space:nowrap}
.subscribe-text b{font-family:var(--serif);font-weight:700}
.email-field{left:334px;top:22px;width:284px;height:23px;border:1px solid var(--white);border-radius:12px}
.email-field span{position:absolute;left:13px;top:7px;font-size:7px;color:var(--white)}
.btn-start{left:526px;top:22px;width:92px;height:23px;background:var(--white);color:var(--blue);border-radius:12px;font-size:6.4px;font-weight:600;letter-spacing:.6px;display:flex;align-items:center;justify-content:center}

/* footer */
.footer-mark{left:224px;top:1059px;font-size:15px}
.footer-call{left:224px;top:1092px;font-size:16.5px;color:var(--blue);font-weight:300}
.footer-mail{left:224px;top:1113px;font-size:7.5px;color:var(--grey);font-weight:300}
.follow{left:457px;top:1062px;font-family:var(--serif);font-weight:700;font-size:12px;color:var(--white)}
.social{top:1095px;width:23px;height:23px;border-radius:50%;border:1px solid var(--red)}
.social.on{background:var(--red)}
.footer-rule{left:18px;top:1168px;width:650px;height:1px;background:#333}
.copyright{left:0;width:686px;top:1180px;text-align:center;font-size:7.5px;color:var(--grey);font-weight:300}
.bolt{background:radial-gradient(ellipse at 55% 50%,rgba(0,170,255,.75),rgba(20,70,220,.35) 40%,rgba(0,0,0,0) 70%)}
</style>
</head>
<body>
<div class="page">

  <header class="site-header abs">
    <a class="nav-link active abs" style="left:56px">HOME</a>
    <a class="nav-link abs" style="left:107px">ABOUT</a>
    <a class="nav-link abs" style="left:162px">MORTY</a>
    <div class="wordmark header-mark abs">BRIMWAVE.live</div>
    <a class="nav-link abs" style="left:496px">RESOURCES</a>
    <a class="nav-link abs" style="left:575px">DEVOTIONALS</a>
    <div class="nav-underline abs"></div>
  </header>

  <section class="hero abs">
    <div class="bolt abs" role="img" aria-label="Glowing blue lightning bolt logo artwork" style="left:20px;top:55px;width:140px;height:150px"></div>
    <svg class="abs" style="left:0;top:0" width="686" height="275" viewBox="0 0 686 275">
      <defs>
        <linearGradient id="heroPhoto" x1="0" y1="0" x2="1" y2="1">
          <stop offset="0" stop-color="#2a2a2a"/>
          <stop offset=".55" stop-color="#1a1a1a"/>
          <stop offset="1" stop-color="#6a3a1a"/>
        </linearGradient>
      </defs>
      <polygon points="245,0 530,0 440,275 156,275" fill="url(#heroPhoto)" role="img" aria-label="Portrait of the host in a black t-shirt beside a motorcycle"/>
      <polygon points="230,35 235,35 166,240 161,240" fill="var(--red)"/>
      <polygon points="521,35 526,35 457,240 452,240" fill="var(--blue)"/>
      <g transform="translate(571,86)">
        <path d="M4 22 A19 19 0 0 1 42 22" fill="none" stroke="var(--red)" stroke-width="3"/>
        <rect x="1" y="22" width="5" height="13" rx="1" fill="var(--red)"/>
        <rect x="40" y="22" width="5" height="13" rx="1" fill="var(--red)"/>
        <path d="M14 17 A12 12 0 0 1 32 17" fill="none" stroke="var(--blue)" stroke-width="2"/>
        <path d="M17.5 20 A7 7 0 0 1 28.5 20" fill="none" stroke="var(--blue)" stroke-width="2"/>
        <rect x="17" y="22" width="12" height="17" rx="6" fill="var(--blue)"/>
        <line x1="23" y1="39" x2="23" y2="44" stroke="var(--blue)" stroke-width="2"/>
        <line x1="17" y1="45" x2="29" y2="45" stroke="var(--blue)" stroke-width="1.5"/>
      </g>
    </svg>
    <div class="hero-text abs">LIFE CHANGING<br>PODCASTS</div>
  </section>

  <section class="about abs">
    <h2 class="section-title about-title abs">About Us</h2>
    <div class="about-copy abs">
      <p>BRIMWAVE.live is all about sharing the good news of Jesus Christ and his redemptive plan of salvation, for all people groups, of every nation. Jesus is the answer to all of our problems, period. He desires that we live a joy filled, purposeful life and he promises to lead and guide us along life's path.</p>
      <p>Its often been said that adversity is the tool that Christ uses to shape our Christian character and we will share many amazing and sometimes miraculous stories and personal testimonies (which we call Brimwaves) ...</p>
    </div>
    <div class="btn btn-discover abs">DISCOVER MORE</div>
  </section>

  <section class="light abs"></section>

  <div class="episodes abs">
    <div class="episode"><svg width="34" height="34" viewBox="0 0 46 46"><use href="#mic"/></svg><div class="episode-date">18-AUG-2020</div><div class="episode-title">Contrary popular belief,<br>Lorem Ipsum</div><div class="episode-bar"></div></div>
    <div class="episode"><svg width="34" height="34" viewBox="0 0 46 46"><use href="#mic"/></svg><div class="episode-date">18-AUG-2020</div><div class="episode-title">Contrary popular belief,<br>Lorem Ipsum</div><div class="episode-bar"></div></div>
    <div class="episode featured"><svg width="34" height="34" viewBox="0 0 46 46"><use href="#micWhite"/></svg><div class="episode-date">18-AUG-2020</div><div class="episode-title">Contrary popular belief,<br>Lorem Ipsum</div><div class="episode-bar"></div></div>
    <div class="episode"><svg width="34" height="34" viewBox="0 0 46 46"><use href="#mic"/></svg><div class="episode-date">18-AUG-2020</div><div class="episode-title">Contrary popular belief,<br>Lorem Ipsum</div><div class="episode-bar"></div></div>
    <div class="episode"><svg width="34" height="34" viewBox="0 0 46 46"><use href="#mic"/></svg><div class="episode-date">18-AUG-2020</div><div class="episode-title">Contrary popular belief,<br>Lorem Ipsum</div><div class="episode-bar"></div></div>
  </div>

  <svg width="0" height="0" style="position:absolute">
    <defs>
      <g id="mic">
        <path d="M4 22 A19 19 0 0 1 42 22" fill="none" stroke="#e42d2f" stroke-width="3"/>
        <rect x="1" y="22" width="5" height="13" rx="1" fill="#e42d2f"/>
        <rect x="40" y="22" width="5" height="13" rx="1" fill="#e42d2f"/>
        <path d="M14 17 A12 12 0 0 1 32 17" fill="none" stroke="#3176b5" stroke-width="2"/>
        <rect x="17" y="21" width="12" height="18" rx="6" fill="#3176b5"/>
        <line x1="23" y1="39" x2="23" y2="44" stroke="#3176b5" stroke-width="2"/>
        <line x1="17" y1="45" x2="29" y2="45" stroke="#3176b5" stroke-width="1.5"/>
      </g>
      <g id="micWhite">
        <path d="M4 22 A19 19 0 0 1 42 22" fill="none" stroke="#fff" stroke-width="3"/>
        <rect x="1" y="22" width="5" height="13" rx="1" fill="#fff"/>
        <rect x="40" y="22" width="5" height="13" rx="1" fill="#fff"/>
        <path d="M14 17 A12 12 0 0 1 32 17" fill="none" stroke="#fff" stroke-width="2"/>
        <rect x="17" y="21" width="12" height="18" rx="6" fill="#fff"/>
        <line x1="23" y1="39" x2="23" y2="44" stroke="#fff" stroke-width="2"/>
        <line x1="17" y1="45" x2="29" y2="45" stroke="#fff" stroke-width="1.5"/>
      </g>
    </defs>
  </svg>

  <h2 class="section-title pastor-title abs">Morty Hallan <span class="dash">–</span> <span class="role">Pastor</span></h2>
  <div class="pastor-copy abs">
    <p>Morty has been involved in motorcycle ministries and outreach for over fifteen years and since 2011 when he became an ordained pastor, under the Riverside Fellowship Network he has officiated many weddings, celebration of life services and baby dedications.</p>
    <p>He pastored a biker church in Surrey for five years and has been a part of a number of outreach groups and ministries over the years which have been focused in the biker world demographic.</p>
  </div>
  <div class="btn btn-explore abs">EXPLORE MORE</div>
  <div class="pastor-frame abs"></div>
  <div class="pastor-photo abs" role="img" aria-label="Black and white photo of the pastor riding a motorcycle"></div>

  <section class="subscribe abs">
    <svg class="abs" style="left:32px;top:20px" width="28" height="28" viewBox="0 0 28 28" fill="none" stroke="#fff" stroke-width="1.2">
      <rect x="1" y="11" width="26" height="16"/>
      <polyline points="1,11 14,20 27,11"/>
      <polyline points="1,27 11,18"/><polyline points="27,27 17,18"/>
      <rect x="5" y="2" width="14" height="13"/>
      <line x1="8" y1="6" x2="16" y2="6"/><line x1="8" y1="9" x2="14" y2="9"/>
      <line x1="22" y1="3" x2="25" y2="1"/><line x1="22" y1="6" x2="26" y2="6"/>
    </svg>
    <div class="subscribe-text abs">Start a Podcast Today. <b>It's FREE.</b></div>
    <div class="email-field abs"><span>Enter Your Email</span></div>
    <div class="btn-start abs">START FOR FREE</div>
  </section>

  <footer>
    <div class="bolt abs" role="img" aria-label="Glowing blue lightning bolt logo artwork" style="left:50px;top:1035px;width:120px;height:120px"></div>
    <div class="wordmark footer-mark abs">BRIMWAVE.live</div>
    <div class="footer-call abs">Call: (09) 5550 1482</div>
    <div class="footer-mail abs">e. brimwavelive.com</div>
    <div class="follow abs">Follow Us</div>
    <div class="social abs" style="left:457px"></div>
    <div class="social on abs" style="left:485px"></div>
    <div class="social abs" style="left:512px"></div>
    <div class="social abs" style="left:539px"></div>
    <svg class="abs" style="left:650px;top:1068px" width="18" height="20" viewBox="0 0 18 20" fill="none" stroke="var(--red)" stroke-width="1.6">
      <polygon points="9,1 17,19 9,14 1,19"/>
    </svg>
    <div class="footer-rule abs"></div>
    <div class="copyright abs">© 2020 Brim Wave. All Right Reserved</div>
  </footer>

</div>
</body>
</html>
```